Improve and Enhance existing design. Roast and Chips

We are an Operations Management company working with cafes, convenience stores, and petrol stations to improve their marketing.

The design work I have for you is to improve, enhance and make ready for hi res printing (with crop marks) in A1 A3 and A4. The attached is the concept and content.

I would like to see examples based on the attached offer.

Thank you.

Bev

```html
<!DOCTYPE html>
<html lang="en">
<head>
<meta charset="utf-8">
<title>Roast Roll &amp; Chips – $8 Only</title>
<link rel="stylesheet" href="https://fonts.googleapis.com/css2?family=EB+Garamond:wght@400;500&family=Archivo+Narrow:wght@700&display=swap">
<style>
  :root {
    --ink: #000000;
    --gold: #ffe500;
    --white: #ffffff;
    --tag-text: #231f20;
    --base-band: #1f1c1d;
    --string: #9a9a9a;
    --backdrop-light: #d6d6d4;
    --table: #2c2c2c;
  }
  html, body {
    margin: 0;
    padding: 0;
    width: 844px;
    height: 1200px;
    overflow: hidden;
    background: var(--ink);
  }
  .poster {
    position: relative;
    width: 844px;
    height: 1200px;
    background: var(--ink);
    overflow: hidden;
  }
  .poster__art {
    position: absolute;
    inset: 0;
    width: 844px;
    height: 1200px;
    display: block;
  }
  .headline-serif {
    font-family: "EB Garamond", "Garamond", serif;
    font-weight: 400;
  }
  .ampersand { fill: var(--white); }
  .headline-gold { fill: var(--gold); }
  .price {
    font-family: "Archivo Narrow", "Arial Narrow", sans-serif;
    font-weight: 700;
    fill: var(--tag-text);
  }
  .price-tag__body { fill: var(--gold); }
  .price-tag__teeth { fill: none; stroke: var(--gold); }
  .price-tag__string { fill: none; stroke: var(--string); stroke-width: 3; }
  .price-tag__hole { fill: var(--ink); stroke: var(--string); stroke-width: 2; }
  .backdrop-strip { fill: url(#stripGradient); }
  .table-top { fill: var(--table); }
  .base-band { fill: var(--base-band); }
</style>
</head>
<body>
  <main class="poster">
    <svg class="poster__art" viewBox="0 0 844 1200" xmlns="http://www.w3.org/2000/svg">
      <defs>
        <linearGradient id="stripGradient" x1="0" y1="0" x2="0" y2="1">
          <stop offset="0" stop-color="#000000"/>
          <stop offset="0.35" stop-color="#bdbdbb"/>
          <stop offset="1" stop-color="#e2e2e0"/>
        </linearGradient>
        <radialGradient id="mealGradient" cx="0.62" cy="0.5" r="0.6">
          <stop offset="0" stop-color="#e8b55a"/>
          <stop offset="0.45" stop-color="#d27a2c"/>
          <stop offset="0.8" stop-color="#8a4a1c"/>
          <stop offset="1" stop-color="#4a2a14"/>
        </radialGradient>
      </defs>

      <!-- scene behind the meal -->
      <rect class="backdrop-strip" x="0" y="800" width="844" height="215"/>
      <rect class="table-top" x="0" y="1012" width="844" height="116"/>

      <!-- meal photograph area -->
      <rect class="meal-photo" x="24" y="597" width="784" height="500" rx="40" fill="url(#mealGradient)"
            role="img" aria-label="Photo of a roast roll burger with lettuce, tomato and cheese beside a wire basket of golden chips"/>

      <!-- bottom band -->
      <rect class="base-band" x="0" y="1128" width="844" height="72"/>

      <!-- headline -->
      <text class="headline-serif ampersand" x="92" y="392" font-size="330">&amp;</text>
      <text class="headline-serif headline-gold" x="247" y="239" font-size="80" textLength="458" lengthAdjust="spacingAndGlyphs">ROAST ROLL</text>
      <text class="headline-serif headline-gold" x="332" y="359" font-size="128" textLength="377" lengthAdjust="spacingAndGlyphs">CHIPS</text>

      <!-- price tag -->
      <path class="price-tag__string" d="M268 338 C 300 350, 296 380, 289 410"/>
      <g class="price-tag">
        <circle class="price-tag__body" cx="289" cy="490" r="90"/>
        <circle class="price-tag__teeth" cx="289" cy="490" r="94" stroke-width="10" stroke-dasharray="6 6.3"/>
        <circle class="price-tag__hole" cx="289" cy="414" r="5"/>
        <text class="price" x="291" y="536" font-size="126" text-anchor="middle">$8</text>
      </g>

      <text class="headline-serif headline-gold" x="414" y="527" font-size="112" textLength="299" lengthAdjust="spacingAndGlyphs">ONLY</text>
    </svg>
  </main>
</body>
</html>
```